Alaska Law Firm Needs a Sticker Design

We need a design for stickers to put on already-printed brochures. We mail the brochures to potential clients so they can learn more about accident-induced injuries, insurance claims, legal representation, and our own law firm.

One of our lawyers wrote a book that provides a helpful overview of personal injury claims. We are offering this book for free to anyone who calls and requests it. Therefore, the sticker design should include one of the following phrases, or something very similar:
a) "Still have questions? Call and request our book-- for free!"
b) "Still have questions about auto accident claims? Call and request our book today."
c) "Still have questions about filing a claim? Call and request a free copy of our book."
d) "Still have questions? Call us today to request a free copy of our book, Clear Lanes Ahead."
e) "To learn more about automobile accidents and insurance, call today and request a free copy of our book."

The sticker should be approximately 3"x3" and may be a circle, square, rectangle, or ellipsis. The sticker will be placed on the back of the folder, which is light blue. We would like the sticker to match the color scheme of our website and the folder.

I will upload an image of the book cover as soon as I obtain it.

Industry/Entity Type

Law Firm

Font styles to use
Serif
Sans Serif

Requirements
Should not have
• Bright colors that aren't already used in the folder design. e.g. no bright orange, pink, chartreuse, turquoise, yellow, red.

```html
<!DOCTYPE html>
<html lang="en">
<head>
<meta charset="utf-8">
<title>Sticker Designs – Free Book Offer</title>
<link href="https://fonts.googleapis.com/css2?family=Marcellus&family=Oswald:wght@700&display=swap" rel="stylesheet">
<style>
  :root {
    --navy: #174372;
    --slate: #6d6d6d;
    --mist: #d9d9d9;
    --white: #ffffff;
  }
  html, body {
    margin: 0;
    padding: 0;
    overflow: hidden;
  }
  body {
    width: 1199px;
    height: 1200px;
    background: var(--navy);
    position: relative;
    font-family: "Marcellus", serif;
  }
  .sticker {
    position: absolute;
    width: 302px;
    height: 302px;
    background: var(--white);
    border-radius: 9px;
    box-shadow: 0 10px 24px rgba(0, 0, 0, 0.35);
    overflow: hidden;
  }
  .sticker__header {
    position: absolute;
    left: 0;
    top: 0;
    width: 302px;
    height: 150px;
    background: var(--slate);
    color: var(--white);
  }
  .sticker__scenery {
    position: absolute;
    left: 155px;
    top: 0;
    width: 147px;
    height: 80px;
    background: linear-gradient(180deg, var(--white) 0%, var(--mist) 100%);
  }
  .header-line {
    position: absolute;
    left: 11px;
    line-height: 1;
    white-space: nowrap;
  }
  .still { font-size: 61px; top: 27px; }
  .have { font-size: 40px; top: 82px; }
  .topic { font-size: 22px; top: 120px; }
  .learn { font-size: 24px; top: 27px; left: 14px; }
  .more { font-size: 40px; top: 47px; left: 14px; }
  .about-auto { font-size: 22px; top: 97px; left: 10px; }
  .and-ins { font-size: 22px; top: 124px; left: 10px; }
  .sticker__offer {
    position: absolute;
    left: 8px;
    top: 158px;
    width: 286px;
    height: 136px;
    background: var(--navy);
    display: flex;
    align-items: center;
    justify-content: center;
    text-align: center;
    color: var(--white);
    font-family: "Oswald", sans-serif;
    font-weight: 700;
    font-size: 36px;
    line-height: 1.17;
  }
  .offer-text { display: inline-block; transform: scaleX(0.8); white-space: nowrap; }
  .offer-text--wide { font-size: 35px; }
  .offer-text--small { font-size: 29px; }
  .offer-text--medium { font-size: 30px; line-height: 1.13; }

  .sticker--a { left: 232px; top: 274px; }
  .sticker--b { left: 615px; top: 274px; }
  .sticker--c { left: 74px; top: 655px; }
  .sticker--d { left: 441px; top: 655px; }
  .sticker--e { left: 818px; top: 655px; }
</style>
</head>
<body>

<div class="sticker sticker--a">
  <div class="sticker__header">
    <div class="sticker__scenery" role="img" aria-label="Snow-capped mountain peaks"></div>
    <span class="header-line still">STILL</span>
    <span class="header-line have">have questions?</span>
  </div>
  <div class="sticker__offer"><span class="offer-text">Call and request<br>our book … for free !</span></div>
</div>

<div class="sticker sticker--b">
  <div class="sticker__header">
    <div class="sticker__scenery" role="img" aria-label="Snow-capped mountain peaks"></div>
    <span class="header-line still">STILL</span>
    <span class="header-line have">have questions</span>
    <span class="header-line topic">about auto accident claims?</span>
  </div>
  <div class="sticker__offer"><span class="offer-text">Call and request<br>our book today</span></div>
</div>

<div class="sticker sticker--c">
  <div class="sticker__header">
    <div class="sticker__scenery" role="img" aria-label="Snow-capped mountain peaks"></div>
    <span class="header-line still">STILL</span>
    <span class="header-line have">have questions</span>
    <span class="header-line topic">about filing a claim?</span>
  </div>
  <div class="sticker__offer"><span class="offer-text offer-text--wide">Call and request<br>a FREE copy of our book</span></div>
</div>

<div class="sticker sticker--d">
  <div class="sticker__header">
    <div class="sticker__scenery" role="img" aria-label="Snow-capped mountain peaks"></div>
    <span class="header-line still">STILL</span>
    <span class="header-line have">have questions</span>
    <span class="header-line topic">about filing a claim?</span>
  </div>
  <div class="sticker__offer"><span class="offer-text offer-text--small">Call us today to request<br>a FREE copy of our book,<br>Clear Lanes Ahead.</span></div>
</div>

<div class="sticker sticker--e">
  <div class="sticker__header">
    <div class="sticker__scenery" role="img" aria-label="Snow-capped mountain peaks"></div>
    <span class="header-line learn">TO LEARN</span>
    <span class="header-line more">MORE</span>
    <span class="header-line about-auto">about automobile accidents</span>
    <span class="header-line and-ins">and insurance …</span>
  </div>
  <div class="sticker__offer"><span class="offer-text offer-text--medium">Call today and request<br>a free copy of our book</span></div>
</div>

</body>
</html>
```